updated documents

Hi i have included a new picture for the about us section, i have also included the updated word document, all changes have been highlighted.

Thanks,

Tobin

```html
<!DOCTYPE html>
<html lang="en">
<head>
<meta charset="utf-8">
<title>Keystone Building Care – Company Profile</title>
<link href="https://fonts.googleapis.com/css2?family=Marcellus+SC&family=Alegreya+Sans:ital,wght@0,400;1,400;1,700&display=swap" rel="stylesheet">
<style>
:root{
  --backdrop:#8a6a52;
  --paper:#e9e5dc;
  --ink:#3f3f3f;
  --body:#4a4a4a;
  --green:#9bc53d;
  --tan:#d3c9b5;
  --tan-edge:#bcb19b;
}
*{margin:0;padding:0;box-sizing:border-box}
html,body{width:1200px;height:1122px;overflow:hidden}
body{background:var(--backdrop);position:relative;font-family:"Alegreya Sans",sans-serif;color:var(--body)}
.sheet{position:absolute;background:var(--paper);box-shadow:0 4px 10px rgba(0,0,0,.35);overflow:hidden}
.cover{left:49px;top:48px;width:678px;height:479px}
.services-a{left:793px;top:52px;width:338px;height:479px}
.about{left:57px;top:589px;width:676px;height:477px}
.services-b{left:797px;top:587px;width:339px;height:479px}
.brand{font-family:"Marcellus SC",serif;color:var(--ink);white-space:nowrap;display:flex;align-items:center;gap:6px}
.brand-dot{width:8px;height:8px;border-radius:50%;background:var(--green);flex:none}
.cover-contact{position:absolute;left:70px;top:196px;width:200px;text-align:center;font-size:7px;line-height:10px;color:var(--ink)}
.cover-contact .brand{font-size:8px;justify-content:center;margin-bottom:8px}
.cover-brand{position:absolute;left:356px;top:256px;font-size:22px;letter-spacing:.3px}
.heading{font-family:"Marcellus SC",serif;color:var(--ink);font-size:17px;display:flex;align-items:center;gap:6px;white-space:nowrap;font-weight:400}
.heading-mark{width:9px;height:9px;background:var(--green);flex:none}
.services-a .heading,.services-b .heading{position:absolute;top:30px;left:0;width:100%;justify-content:center}
.service-list{position:absolute;left:21px;width:296px;top:84px}
.services-b .service-list{top:82px}
.service{margin-bottom:9px}
.service h3{font-size:7px;font-style:italic;font-weight:700;color:#222;line-height:10px}
.service p{font-size:6.9px;font-style:italic;line-height:9.4px;text-align:justify}
.sheet-foot{position:absolute;bottom:28px;left:0;width:100%;justify-content:center;font-size:9.5px}
.about .heading{position:absolute;left:118px;top:157px}
.about-copy{position:absolute;left:32px;top:196px;width:278px;font-size:7.8px;font-style:italic;line-height:13.6px;text-align:justify}
.about-copy p{margin-bottom:13.6px}
.about-curve{position:absolute;left:0;top:0;width:100%;height:100%}
.about-brand{position:absolute;left:477px;top:418px;font-size:12px}
</style>
</head>
<body>

<section class="sheet cover">
  <div class="cover-contact">
    <div class="brand"><span class="brand-dot"></span>Keystone Building Care</div>
    <p>Phone: 0400 123 456</p>
    <p>Email: tobin@keystonebc.com.au</p>
    <p>Website: www.keystonebuildingcare.com</p>
    <p>Social: @keystonebuildingcare</p>
  </div>
  <div class="brand cover-brand"><span class="brand-dot"></span>Keystone Building Care</div>
</section>

<section class="sheet services-a">
  <h2 class="heading"><span class="heading-mark"></span>Our Services</h2>
  <div class="service-list">
    <div class="service"><h3>Building repairs and Maintenance</h3><p>The team at Keystone Building Care have extensive skills and experience in both internal and external building repairs and maintenance. Installation and repairs to floor and ceilings systems, doors/locks, appliance repairs, whiteboards, TV screens, picture hanging, patching and paint, vandal repairs, workstations and joinery, plumbing and electrical.</p></div>
    <div class="service"><h3>Electrical</h3><p>Keystone Building Care provides a wide range of electrical services ranging from Test and tag, Mains services, Switchboard installations, fault finding, RCD testing, data cabling/patching, electrical upgrades and lighting.</p></div>
    <div class="service"><h3>Planned preventative maintenance</h3><p>Keystone Building Care offer planned preventive maintenance specifically tailored to the client's requirements. Planned maintenance schedules can be created to prevent breakdowns and costly reactive maintenance in the future. Maintenance programs can include floor and ceiling repairs, light bulb replacements, Test and tagging, Storm water and gutter cleaning.</p></div>
    <div class="service"><h3>Painting</h3><p>Keystone Building Care pride ourselves in quality and detail ensuring the very best results while being a cost effective and efficient.</p></div>
    <div class="service"><h3>Signage</h3><p>Keystone Building Care have an experience signage team that specialize in both internal and external signage, decals, promotional banners, window frosting, company logos and design.</p></div>
    <div class="service"><h3>Office layout changes</h3><p>If you are looking to make some changes to your office either big or small our team can assist with Workstation reconfiguration, internal demolition, Partition/wall installations and even complete office relocations.</p></div>
    <div class="service"><h3>Appliance repairs</h3><p>Keystone Building Care can repair and replace all of your office appliance's ranging from dishwashers and microwaves to monitors, TV's and projectors.</p></div>
  </div>
  <div class="brand sheet-foot"><span class="brand-dot"></span>Keystone Building Care</div>
</section>

<section class="sheet about">
  <svg class="about-curve" viewBox="0 0 676 477" preserveAspectRatio="none" aria-hidden="true">
    <path d="M336 477 C420 390 520 300 676 284 L676 477 Z" fill="var(--tan)"/>
    <path d="M336 477 C420 390 520 300 676 284" fill="none" stroke="var(--tan-edge)" stroke-width="1.5"/>
  </svg>
  <h2 class="heading"><span class="heading-mark"></span>About Us</h2>
  <div class="about-copy">
    <p>Keystone Building Care is an Adelaide based company providing general building and office maintenance and refurbishments. We pride ourselves in delivering cost affective high quality services with minimal disturbance to tenants and their occupants.</p>
    <p>Keystone Building Care provides a wide range of services including all major trades Electrical, Data, Plumbing, carpentry, landscaping, and more. With all trades available we can manage their work as required. We also provide preventive maintenance programs to help reduce future reactive works. Our Team are have all undertaken police checks and are white card accredited.</p>
  </div>
  <div class="brand about-brand"><span class="brand-dot"></span>Keystone Building Care</div>
</section>

<section class="sheet services-b">
  <h2 class="heading"><span class="heading-mark"></span>Our Services</h2>
  <div class="service-list">
    <div class="service"><h3>Cleaning</h3><p>Our team offer both internal and external cleaning services including carpark cleaning, window cleaning, carpet dry cleaning, and general office cleaning.</p></div>
    <div class="service"><h3>Rubbish removal/Recycling</h3><p>Keystone Building Care specialize in office rubbish removal, We have a solution to all your rubbish removal needs; including, electronic waste recycling (PCs, monitors, printers, cables etc.), Basement access skip bins, wheelie bins of various sizes, internal demolition services, workstation/furniture removal, rubbish removal/cleanup services.</p></div>
    <div class="service"><h3>Plumbing</h3><p>Our Plumbing team are experienced and available 24/7 for all your plumbing requirements. Our plumbing services include, water boiler/chiller unit installs and repairs, blocked drains and toilets, roof work and gas fitting.</p></div>
    <div class="service"><h3>Grounds keeping</h3><p>Let us help with your grounds keeping, our services include, lawn mowing and garden care, carpark sweeping, tree pruning, line marking, gutter cleaning, landscaping, bird and pest management, fencing installs and repairs.</p></div>
    <div class="service"><h3>Carpentry</h3><p>Keystone Building Care have a dedicated carpentry team that can assist with all your requirements including Partitioning, cupboard installations and all repairs and modifications.</p></div>
    <div class="service"><h3>Floor /ceiling</h3><p>We can provide floor and ceiling repairs to all types of systems including, suspended ceiling systems and raised floors, ceiling/floor tile replacement, carpet and vinyl replacements and repairs, ceiling access hatches and air vent installs.</p></div>
  </div>
  <div class="brand sheet-foot"><span class="brand-dot"></span>Keystone Building Care</div>
</section>

</body>
</html>
```